Banner Ad Design Project 300x250 NOW

I need 5 300x250 banners done now. 5 for each campaign.
I need them done in 3 hours if you can do it. Lets go.
So 5 banners 300x250 for KVR 5 for Lornfield Institute of Sound and Screen, etc.
Here are our landing pages for messaging background.
Here are the numbers to put on the initial set for each:
KVR Direct (866) 555-0142
http://www.nearbyshopratings.example/KVR-40318.html
I want to focus the messaging on like an image I will attach to this project. No free system though, $99 next day install instead.
Lornfield Institute of Sound and Screen (866) 555-0187
http://www.nearbyshopratings.example/The-Lornfield-Institute-of-Sound-and-Screen-Production-40324.html
The Quillmark School (866) 555-0123
http://quickpagehostery.example/_PROJECT_/quillmark-schools/index.php
Renewal Nearby (866) 555-0169
http://nearbyshopratings.example/Renewal-Nearby-40303.html
Clearpath Debtfix (866) 555-0194
http://www.clearpathdebtfix.example/
Payment through ArtHive only. Will need all source files emailed to me along with creative final.
Thank you!
Gareth
Radio

```html
<!DOCTYPE html>
<html lang="en">
<head>
<meta charset="utf-8">
<title>Clearpath Debtfix — 300x250 Banner Set</title>
<link rel="stylesheet" href="https://fonts.googleapis.com/css2?family=Jost:wght@400;500&family=Oswald:wght@500&family=Archivo+Black&family=Arimo:wght@700&family=Gelasio:wght@700&display=swap">
<style>
  :root{
    --stage-top:#161616;
    --stage-bottom:#4a4a4a;
    --teal:#1c9a89;
    --teal-dark:#127767;
    --teal-light:#3ab3a0;
    --plum:#8c1d6b;
    --plum-dark:#6e1150;
    --plum-light:#c3589d;
    --yellow:#f6e21e;
    --gold:#f1b000;
    --gold-light:#f8d90a;
    --orange:#ee7f12;
    --orange-light:#f7a11c;
    --ink:#111;
    --grey:#555;
    --white:#fff;
    --photo-light:#8a8f94;
    --photo-dark:#5b6066;
  }
  html,body{margin:0;padding:0;width:1200px;height:780px;overflow:hidden;background:var(--stage-top);}
  .stage{
    width:1024px;height:666px;position:relative;overflow:hidden;
    transform:scale(1.171875);transform-origin:0 0;
    background:linear-gradient(180deg,var(--stage-top) 0%,var(--stage-bottom) 100%);
  }
  .banner{position:absolute;width:300px;height:250px;overflow:hidden;font-family:"Jost",sans-serif;}
  .banner--a{left:55px;top:83px;background:var(--white);}
  .banner--b{left:367px;top:83px;background:linear-gradient(180deg,var(--teal-light),var(--teal-dark));}
  .banner--c{left:682px;top:83px;background:linear-gradient(180deg,#fff 0%,#e6e6e6 60%,#fff 100%);}
  .banner--d{left:205px;top:372px;background:var(--white);box-sizing:border-box;border:5px solid var(--teal);}
  .banner--e{left:548px;top:372px;background:linear-gradient(180deg,var(--plum-dark),var(--plum-light));}
  .abs{position:absolute;}

  .brand{position:absolute;display:flex;flex-direction:column;}
  .brand__name{display:flex;align-items:center;gap:5px;font-family:"Jost",sans-serif;font-weight:500;font-size:19px;color:var(--plum);line-height:1;white-space:nowrap;}
  .brand__mark{width:8px;height:8px;background:var(--plum);}
  .brand__tag{font-family:"Arimo",sans-serif;font-weight:700;font-size:6.5px;color:#444;margin-top:4px;margin-left:13px;white-space:nowrap;}

  .headline{font-family:"Oswald",sans-serif;font-weight:500;line-height:1;letter-spacing:.5px;white-space:nowrap;}
  .body-copy{font-family:"Jost",sans-serif;line-height:1.1;white-space:nowrap;}
  .call{font-family:"Arimo",sans-serif;font-weight:700;white-space:nowrap;}
  .phone{font-family:"Gelasio",serif;font-weight:700;white-space:nowrap;line-height:1;}
  .protect{font-family:"Archivo Black",sans-serif;color:var(--yellow);font-size:17px;line-height:1;white-space:nowrap;}

  .photo{position:absolute;background:linear-gradient(180deg,var(--photo-light),var(--photo-dark));}

  .ribbon{position:absolute;background:linear-gradient(180deg,var(--teal-light),var(--teal-dark));box-shadow:0 2px 3px rgba(0,0,0,.3);}
</style>
</head>
<body>
<div class="stage">

  <section class="banner banner--a">
    <div class="abs" style="left:0;top:103px;width:300px;height:147px;background:linear-gradient(180deg,var(--gold),var(--gold-light));"></div>
    <div class="brand" style="left:8px;top:30px;">
      <div class="brand__name"><span class="brand__mark"></span>Clearpath Debtfix</div>
      <div class="brand__tag">Bankruptcy Attorneys Nationwide.</div>
    </div>
    <div class="headline abs" style="right:8px;top:12px;font-size:33px;color:var(--teal);text-align:center;line-height:1.1;">GOT<br>DEBT?</div>
    <div class="body-copy abs" style="left:0;width:300px;top:111px;text-align:center;font-size:21px;color:var(--ink);line-height:1.4;">FIND OUT HOW TO<br>PROTECT YOURSELF</div>
    <div class="call abs" style="left:0;width:300px;top:182px;text-align:center;font-size:17px;color:var(--ink);">Call Now!</div>
    <div class="abs" style="left:50px;top:209px;width:202px;height:34px;background:var(--plum);"></div>
    <div class="phone abs" style="left:50px;width:202px;top:215px;text-align:center;font-size:21px;color:var(--white);">(866) 555-0194</div>
  </section>

  <section class="banner banner--b">
    <svg class="abs" style="left:0;top:0" width="300" height="80" viewBox="0 0 300 80" aria-hidden="true">
      <path d="M0 0H276V66C190 52 90 54 0 72Z" fill="#fff"/>
    </svg>
    <div class="brand" style="left:66px;top:15px;">
      <div class="brand__name"><span class="brand__mark"></span>Clearpath Debtfix</div>
      <div class="brand__tag">Bankruptcy Attorneys Nationwide.</div>
    </div>
    <div class="photo" role="img" aria-label="Photo of a smiling businesswoman with arms crossed" style="left:192px;top:40px;width:108px;height:210px;"></div>
    <div class="headline abs" style="left:6px;top:84px;font-size:32px;color:var(--yellow);">GOT DEBT?</div>
    <div class="body-copy abs" style="left:6px;top:127px;font-size:18px;color:var(--white);">Find out how to<br>protect yourself</div>
    <div class="call abs" style="left:6px;top:182px;font-size:18px;color:var(--white);">Call Now!</div>
    <div class="abs" style="left:0;top:210px;width:192px;height:40px;background:linear-gradient(90deg,var(--yellow),#fff27a);"></div>
    <div class="phone abs" style="left:6px;top:220px;font-size:20px;color:var(--ink);">(866) 555-0194</div>
  </section>

  <section class="banner banner--c">
    <div class="brand" style="left:14px;top:12px;">
      <div class="brand__name"><span class="brand__mark"></span>Clearpath Debtfix</div>
      <div class="brand__tag">Bankruptcy Attorneys Nationwide.</div>
    </div>
    <div class="ribbon" style="left:105px;top:66px;width:195px;height:53px;border-radius:4px 0 0 4px;"></div>
    <div class="headline abs" style="left:116px;top:72px;font-size:36px;color:var(--white);">GOT DEBT?</div>
    <div class="ribbon" style="left:0;top:128px;width:300px;height:53px;"></div>
    <div class="body-copy abs" style="left:9px;top:135px;font-size:15px;color:var(--white);">FIND OUT HOW TO</div>
    <div class="protect abs" style="left:9px;top:154px;">PROTECT YOURSELF</div>
    <div class="photo" role="img" aria-label="Photo of a smiling young woman" style="left:236px;top:112px;width:60px;height:69px;"></div>
    <div class="abs" style="left:0;top:205px;width:300px;height:45px;background:linear-gradient(180deg,var(--orange-light),var(--orange));"></div>
    <div class="phone abs" style="left:0;width:300px;top:212px;text-align:center;font-size:28px;color:var(--white);">(866) 555-0194</div>
  </section>

  <section class="banner banner--d">
    <div class="brand" style="left:10px;top:5px;">
      <div class="brand__name"><span class="brand__mark"></span>Clearpath Debtfix</div>
      <div class="brand__tag">Bankruptcy Attorneys Nationwide.</div>
    </div>
    <div class="ribbon" style="left:97px;top:55px;width:198px;height:53px;border-radius:4px 0 0 4px;"></div>
    <div class="headline abs" style="left:108px;top:61px;font-size:36px;color:var(--white);">GOT DEBT?</div>
    <div class="ribbon" style="left:0;top:126px;width:295px;height:53px;"></div>
    <div class="body-copy abs" style="left:4px;top:133px;font-size:15px;color:var(--white);">FIND OUT HOW TO</div>
    <div class="protect abs" style="left:4px;top:152px;">PROTECT YOURSELF</div>
    <div class="photo" role="img" aria-label="Photo of a smiling young woman" style="left:229px;top:108px;width:60px;height:71px;"></div>
    <div class="call abs" style="left:0;width:290px;top:185px;text-align:center;font-size:19px;color:var(--grey);">Call Now!</div>
    <div class="phone abs" style="left:0;width:290px;top:209px;text-align:center;font-size:27px;color:var(--plum);">(866) 555-0194</div>
  </section>

  <section class="banner banner--e">
    <svg class="abs" style="left:0;top:0" width="300" height="80" viewBox="0 0 300 80" aria-hidden="true">
      <path d="M20 0H278V60C200 68 110 72 20 76Z" fill="#fff"/>
    </svg>
    <div class="brand" style="left:68px;top:15px;">
      <div class="brand__name"><span class="brand__mark"></span>Clearpath Debtfix</div>
      <div class="brand__tag">Bankruptcy Attorneys Nationwide.</div>
    </div>
    <div class="photo" role="img" aria-label="Photo of a smiling businesswoman with arms crossed" style="left:190px;top:40px;width:110px;height:210px;"></div>
    <div class="headline abs" style="left:8px;top:86px;font-size:31px;color:var(--white);">GOT DEBT?</div>
    <div class="body-copy abs" style="left:8px;top:124px;font-size:19px;color:var(--yellow);">Find out how to<br>protect yourself</div>
    <div class="call abs" style="left:44px;top:190px;font-size:17px;color:var(--white);">Call Now!</div>
    <div class="abs" style="left:6px;top:213px;width:180px;height:31px;background:linear-gradient(90deg,var(--yellow),#fff27a);"></div>
    <div class="phone abs" style="left:10px;top:220px;font-size:19px;color:var(--ink);">(866) 555-0194</div>
  </section>

</div>
</body>
</html>
```